LAW FIRM - RE-DESIGN - (professional, excellence, tradition and innovation)

We are a premier law firm in New South Wales, Australia. We pride ourselves on being cutting edge and up to date in our market.

Our firm formed in 1874 and has a particularly strong tradition within it's geographic footprint. acting for clients over multiple generations. Despite our regional background, our reputation for excellence has enable us to remain highly visible in a large area.

We have invested heavily in ensuring future planning of this business, and do so on a recurring basis. This has lead to a review of our existing web site.

Although serviceable we feel our previous website is out-of-date and not as in touch with the modern market. We are aware that for the emerging clients a web site is often the face of a firm and a failure to hold attention on the first page may fail to capture the client.

We are seeking designs to communicate the core values of professionalism and excellence. At the same time as maintaining traditional country values of honesty, integrity and hard work we strive to embrace changes to the law and technology.

Target Market(s)

Clients of Law Firm

Industry/Entity Type

Law Firm

Coding

Coded - Design and coding required

Number of Pages Required

5+ page

Requirements
Must have
• A strong sense of professionalism and excellence with a careful balance between traditional values and innovation.
Nice to have
• We have included within our design brief links to top competitors sites to assist for design concepts.

```html
<!DOCTYPE html>
<html lang="en">
<head>
<meta charset="utf-8">
<title>Harlow Law</title>
<link rel="stylesheet" href="https://fonts.googleapis.com/css2?family=Roboto:wght@400;500;700&family=Source+Sans+3:wght@400;600&display=swap">
<style>
:root{
  --black:#000;
  --footer:#0b0b0b;
  --white:#fff;
  --nav-text:#555;
  --navy:#1d3a8c;
  --blue:#0a7bc0;
  --orange:#e09a25;
  --grey-text:#8a8a8a;
  --dark-text:#333;
  --field-border:#9a9a9a;
  --arrow-bg:#b5b5b5;
  --link:#1f3fa8;
}
*{margin:0;padding:0;box-sizing:border-box}
html,body{width:1200px;height:2809px;overflow:hidden;background:var(--white)}
body{font-family:"Source Sans 3",Arial,sans-serif;color:var(--dark-text)}
.page{position:relative;width:1200px;height:2809px;overflow:hidden}
.abs{position:absolute}

.top-strip{left:0;top:0;width:1200px;height:27px;background:var(--black)}
.site-nav{left:0;top:27px;width:1200px;height:69px;background:var(--white)}
.brand{position:absolute;left:243px;top:18px;font:700 24px/32px "Source Sans 3",sans-serif;color:var(--navy)}
.nav-links{position:absolute;top:25px;left:0;font:400 13px/18px Roboto,sans-serif;color:var(--nav-text)}
.nav-links span{position:absolute;white-space:nowrap}
.search{position:absolute;left:992px;top:24px;display:flex;align-items:center;gap:10px;font:400 12px Roboto,sans-serif;color:#999}

.hero{left:0;top:96px;width:1200px;height:484px;background:linear-gradient(100deg,#2a2422 0%,#5b4e47 35%,#8b7b72 55%,#a24a1c 85%,#6a2a10 100%)}
.hero-title{left:0;top:232px;width:1200px;text-align:center;font:700 44px/53px Roboto,sans-serif;color:var(--white)}
.hero-sub{left:396px;top:344px;font:400 24px/27px Roboto,sans-serif;color:var(--white)}
.btn-read{left:539px;top:422px;width:122px;height:37px;background:var(--blue);color:var(--white);font:400 15px/37px Roboto,sans-serif;text-align:center}
.hero-arrow{top:306px;width:63px;height:63px;background:rgba(0,0,0,.45);display:flex;align-items:center;justify-content:center}

.feature{top:580px;height:236px;color:var(--white);text-align:center}
.feature h3{position:absolute;top:22px;left:0;width:100%;font:400 22px/28px "Source Sans 3",sans-serif}
.feature p{position:absolute;top:70px;left:50%;transform:translateX(-50%);font:400 11.5px/15px "Source Sans 3",sans-serif}
.btn-more{position:absolute;top:159px;left:50%;transform:translateX(-50%);width:86px;height:26px;background:var(--white);color:var(--orange);font:400 12px/26px "Source Sans 3",sans-serif}
.f-services{left:0;width:468px;background:linear-gradient(160deg,#4a2e1f,#1e130d)}
.f-people{left:468px;width:266px;background:linear-gradient(160deg,#6a6a6a,#2b2b2b)}
.f-community{left:734px;width:466px;background:linear-gradient(180deg,#3f79b9,#9a5f46 70%,#7a3e2a)}

.history-img{left:0;top:816px;width:678px;height:449px;background:linear-gradient(100deg,#6e6e6e 0%,#b8b8b8 45%,#e6e6e6 80%,#fafafa 100%)}
.history{left:533px;top:842px;width:575px}
.history h2{font:400 34px/40px "Source Sans 3",sans-serif;color:#444;margin-bottom:16px}
.history p{font:400 14.5px/19px "Source Sans 3",sans-serif;color:var(--grey-text);margin-bottom:19px}

.section-title{left:0;width:1200px;text-align:center;font:400 32px/40px "Source Sans 3",sans-serif;color:#333}
.title-rule{left:563px;top:1370px;width:74px;height:3px;background:var(--navy)}
.staff-photo{top:1410px;width:227px;height:289px;background:linear-gradient(180deg,#7a4b22 0%,#4a2c16 50%,#1c1c1c 100%)}
.staff-name{top:1716px;font:400 15px/18px "Source Sans 3",sans-serif;color:var(--orange)}
.staff-role{top:1736px;font:400 11.5px/14px "Source Sans 3",sans-serif;color:#444}
.staff-arrow{top:1523px;width:63px;height:63px;background:var(--arrow-bg);display:flex;align-items:center;justify-content:center}

.divider{left:61px;top:1792px;width:1080px;height:1px;background:#aaa}
.contact-intro{left:0;top:1895px;width:1200px;text-align:center;font:400 15px/27px "Source Sans 3",sans-serif;color:#444}
.field{left:57px;width:1082px;border:3px solid var(--field-border);background:var(--white);font:italic 400 12px Roboto,sans-serif;color:#999;text-align:center}
.btn-send{left:485px;top:2358px;width:230px;height:50px;background:var(--orange);color:var(--white);font:400 20px/50px "Source Sans 3",sans-serif;text-align:center}

.site-footer{left:0;top:2490px;width:1200px;height:319px;background:var(--footer)}
.footer-brand{position:absolute;left:126px;top:100px;font:700 56px/60px "Source Sans 3",sans-serif;color:#6d6d6d}
.office{position:absolute;top:97px;font:400 14px/19.3px "Source Sans 3",sans-serif;color:var(--white);text-transform:uppercase}
.office h4{font:400 14px/19px "Source Sans 3",sans-serif;margin-bottom:16px}
.office .map{color:var(--link)}
</style>
</head>
<body>
<div class="page">
  <div class="abs top-strip"></div>

  <header class="abs site-nav">
    <div class="brand">Harlow Law</div>
    <nav class="nav-links">
      <span style="left:468px">About us</span>
      <span style="left:554px">Services</span>
      <span style="left:636px">Our People</span>
      <span style="left:732px">FAQ's</span>
      <span style="left:797px">Contact Us</span>
    </nav>
    <div class="search">
      <svg width="13" height="13" viewBox="0 0 13 13"><circle cx="5.3" cy="5.3" r="3.8" fill="none" stroke="#1d3a8c" stroke-width="2"/><line x1="8.2" y1="8.2" x2="12" y2="12" stroke="#1d3a8c" stroke-width="2.2"/></svg>
      <span>Search Here...</span>
    </div>
  </header>

  <section>
    <div class="abs hero" role="img" aria-label="Close-up of a lawyer's hands holding and signing a legal document"></div>
    <h1 class="abs hero-title">Lorem ipsum dolor sit amet<br>consectetur adipisicing elit</h1>
    <p class="abs hero-sub">Accusantium doloremque laudantium<br>totam rem aperiam, eaque ipsa...</p>
    <div class="abs btn-read">Read more</div>
    <div class="abs hero-arrow" style="left:25px"><svg width="16" height="20" viewBox="0 0 16 20"><polyline points="11,3 4,10 11,17" fill="none" stroke="#fff" stroke-width="3"/></svg></div>
    <div class="abs hero-arrow" style="left:1112px"><svg width="16" height="20" viewBox="0 0 16 20"><polyline points="5,3 12,10 5,17" fill="none" stroke="#fff" stroke-width="3"/></svg></div>
  </section>

  <section>
    <div class="abs feature f-services" role="img" aria-label="Gavel resting on a wooden desk">
      <h3>Our Services</h3>
      <p style="width:340px">We offer a range of legal services throughout the New England Region and beyond. It is our firm's policy to refer clients to the person within the firm that has the necessary expertise to gain the best outcome for their particular matter</p>
      <div class="btn-more">More</div>
    </div>
    <div class="abs feature f-people" role="img" aria-label="Black and white photo of a professional team">
      <h3>Our People</h3>
      <p style="width:248px">We employ highly competent people with a wide range of skills. Our team of both Professional and Support Staff have many years of experience and many areas of expertise</p>
      <div class="btn-more">More</div>
    </div>
    <div class="abs feature f-community" role="img" aria-label="Crowd of raised hands against a blue sky">
      <h3>Community</h3>
      <p style="width:230px">Harlow Law is proud to support and be part of these great community events and programs</p>
      <div class="btn-more">More</div>
    </div>
  </section>

  <section>
    <div class="abs history-img" role="img" aria-label="Businessman with a briefcase walking up stone steps"></div>
    <div class="abs history">
      <h2>Our History</h2>
      <p>Harlow Law (formerly known as Ashcombe Pardoe &amp; Jennings) has been part of the New England Region of New South Wales for over a century.</p>
      <p>Harlow Law has been in existence since 1874 originally starting out as the firm Walter Hensley of Glen Arden. In 1894 Walter Hensley was acquired by Colonel RJ Ashcombe. The firm became known as RW Ashcombe &amp; Co. until early 1970 when it became Ashcombe &amp; Co, Ashcombe Pardoe &amp; Co in 1979 and Ashcombe Pardoe &amp; Jennings in 1982.</p>
      <p>Harlow Law is proud of its long and distinguished history as a regional law firm and its service to the region.</p>
      <p>In December 1999, the firm opened an office in Wexmoor taking over the practice of LM Carver &amp; Associates. This was followed by the incorporation of Tenbury &amp; Co in December 2000 and the Ashford Vale office moved to larger premises in Marden Street.</p>
    </div>
  </section>

  <section>
    <h2 class="abs section-title" style="top:1307px">Our Staff</h2>
    <div class="abs title-rule"></div>
    <div class="abs staff-arrow" style="left:25px"><svg width="16" height="20" viewBox="0 0 16 20"><polyline points="11,3 4,10 11,17" fill="none" stroke="#fff" stroke-width="2.5"/></svg></div>
    <div class="abs staff-arrow" style="left:1112px"><svg width="16" height="20" viewBox="0 0 16 20"><polyline points="5,3 12,10 5,17" fill="none" stroke="#fff" stroke-width="2.5"/></svg></div>

    <div class="abs staff-photo" style="left:193px" role="img" aria-label="Portrait of a staff member in front of law books"></div>
    <div class="abs staff-name" style="left:193px">John Doe</div>
    <div class="abs staff-role" style="left:193px">Manager</div>

    <div class="abs staff-photo" style="left:487px" role="img" aria-label="Portrait of a staff member in front of law books"></div>
    <div class="abs staff-name" style="left:487px">John Doe</div>
    <div class="abs staff-role" style="left:487px">Manager</div>

    <div class="abs staff-photo" style="left:782px" role="img" aria-label="Portrait of a staff member in front of law books"></div>
    <div class="abs staff-name" style="left:782px">John Doe</div>
    <div class="abs staff-role" style="left:782px">Manager</div>
  </section>

  <div class="abs divider"></div>

  <section>
    <h2 class="abs section-title" style="top:1832px">CONTACT US</h2>
    <p class="abs contact-intro">I've heard some variation of this question many times over the past couple of months. You likely know that a haiku is a form of poetry;<br>you might even know that it's composed of two lines</p>
    <div class="abs field" style="top:1997px;height:54px;line-height:48px">name</div>
    <div class="abs field" style="top:2062px;height:54px;line-height:48px">email</div>
    <div class="abs field" style="top:2129px;height:53px;line-height:47px">subject</div>
    <div class="abs field" style="top:2194px;height:136px;padding-top:10px">message</div>
    <div class="abs btn-send">SEND</div>
  </section>

  <footer class="abs site-footer">
    <div class="footer-brand">Harlow Law</div>
    <div class="office" style="left:443px">
      <h4>Ashford Vale</h4>
      Suite 9, Keller's Arcade<br>Ashford Vale, NSW 2901<br>02 5550 4500<br>02 5550 4533<br><span class="map">See map</span>
    </div>
    <div class="office" style="left:709px">
      <h4>Glen Arden</h4>
      218 Linden Street<br>Glen Arden NSW 2902<br>02 5550 2222<br>02 5550 2244<br><span class="map">See map</span>
    </div>
    <div class="office" style="left:936px">
      <h4>Caldra</h4>
      74 Fenwick Street<br>Caldra NSW 2903<br>02 5550 4500<br>(By appointment)<br><span class="map">See map</span>
    </div>
  </footer>
</div>
</body>
</html>
```